Disposable Mini Sauce Pot Design for Asian Chain Food Brands

We operate a Hainan Chicken Rice takeout brand under the name Wokly8, with our official website: www.Wokly8.com.
We offer four signature house sauces and are launching brand-new packaging for our sauce line. We require custom graphic designs exclusively for the sauce cup lids.
Product Material & Base Specs
The sauce cups are made of PP plastic, available in two translucent base options: Translucent White and Translucent Orange.
Four Sauce Varieties for Individual Lid Designs
1. Red Sauce – Fried Sweet Chili Sauce
2.Green Sauce – Scallion Oil Dressing
3.Sweet Soy Sauce
4.Sweet Red Sauce (Special for Fried Chicken)
Differentiate each sauce lid design through unique graphics, typography, or illustrative elements for easy customer identification.
The marking NET WT 2 OZ must be clearly printed on every lid.
**There is no need to print full descriptive text or the full name of the sauces on each lid; the design only needs to clearly differentiate the four sauce varieties.
**Please reference the original design style and brand color palette shown on our official website, and feel free to fully unleash your creativity.
Look and feel
Each slider illustrates characteristics of the customer's brand and the style your logo design should communicate.

```html
<!DOCTYPE html>
<html lang="en">
<head>
<meta charset="utf-8">
<title>Wokly8 Sauce Lid Labels</title>
<link href="https://fonts.googleapis.com/css2?family=Righteous&family=Lilita+One&display=swap" rel="stylesheet">
<style>
  :root {
    --page: #f9f9f9;
    --red: #d9251d;
    --red-shade: #b91e18;
    --green: #86c128;
    --green-shade: #6fa321;
    --black: #231f20;
    --orange: #e2781b;
    --white: #ffffff;
  }
  html, body {
    margin: 0;
    padding: 0;
    width: 1200px;
    height: 782px;
    overflow: hidden;
    background: var(--page);
  }
  .lid-row {
    position: relative;
    width: 1200px;
    height: 782px;
  }
  .lid {
    position: absolute;
    top: 300px;
    width: 236px;
    height: 267px;
    display: block;
  }
  .lid--red { left: 39px; }
  .lid--green { left: 342px; }
  .lid--soy { left: 632px; }
  .lid--sweet-red { left: 922px; }

  .display { font-family: "Righteous", "Arial Black", sans-serif; }
  .weight { font-family: "Lilita One", "Arial Black", sans-serif; }
  .fill-white { fill: var(--white); }
  .fill-orange { fill: var(--orange); }
  .bg-red { fill: var(--red); }
  .bg-green { fill: var(--green); }
  .bg-black { fill: var(--black); }
  .bg-orange { fill: var(--orange); }
  .decor-red { fill: var(--red-shade); opacity: 0.5; }
  .decor-green { fill: var(--green-shade); opacity: 0.55; }
</style>
</head>
<body>
<main class="lid-row">

  <!-- Red Sauce -->
  <svg class="lid lid--red" viewBox="0 0 236 267" aria-label="Red Sauce lid">
    <defs><clipPath id="clip-red"><rect width="236" height="267" rx="10"/></clipPath></defs>
    <g clip-path="url(#clip-red)">
      <rect class="bg-red" width="236" height="267"/>
      <rect class="decor-red" x="10" y="90" width="216" height="160" rx="40" role="img" aria-label="Faint chili pepper illustrations"/>
      <text class="display fill-white" x="-2" y="88" font-size="128" textLength="240" lengthAdjust="spacingAndGlyphs">Red</text>
      <text class="display fill-white" x="118" y="120" font-size="32" text-anchor="middle" textLength="204" lengthAdjust="spacingAndGlyphs">Garlic~Chili</text>
      <text class="display fill-white" x="-2" y="192" font-size="96" textLength="240" lengthAdjust="spacingAndGlyphs">Sauce</text>
      <text class="display fill-white" x="118" y="216" font-size="15" text-anchor="middle" textLength="226" lengthAdjust="spacingAndGlyphs">Spicy, Tangy, Sweet &amp;Garlicky</text>
      <text class="display fill-white" x="22" y="246" font-size="18">Wokly8</text>
      <text class="weight fill-white" x="223" y="246" font-size="16" text-anchor="end">NET WT 2 OZ</text>
    </g>
  </svg>

  <!-- Green Sauce -->
  <svg class="lid lid--green" viewBox="0 0 236 267" aria-label="Green Sauce lid">
    <defs><clipPath id="clip-green"><rect width="236" height="267" rx="10"/></clipPath></defs>
    <g clip-path="url(#clip-green)">
      <rect class="bg-green" width="236" height="267"/>
      <rect class="decor-green" x="40" y="40" width="150" height="180" rx="60" transform="rotate(35 115 130)" role="img" aria-label="Faint scallion illustration"/>
      <text class="display fill-white" x="-1" y="63" font-size="84" textLength="238" lengthAdjust="spacingAndGlyphs">Green</text>
      <text class="display fill-white" x="-1" y="131" font-size="88" textLength="238" lengthAdjust="spacingAndGlyphs">Sauce</text>
      <text class="display fill-white" x="118" y="172" font-size="24" text-anchor="middle" textLength="222" lengthAdjust="spacingAndGlyphs">Ginger~Scallion Oil</text>
      <text class="display fill-white" x="118" y="206" font-size="15" text-anchor="middle" textLength="228" lengthAdjust="spacingAndGlyphs">Salty, Aromatic &amp; Deeply Savory</text>
      <text class="display fill-white" x="20" y="246" font-size="18">Wokly8</text>
      <text class="weight fill-white" x="223" y="246" font-size="16" text-anchor="end">NET WT 2 OZ</text>
    </g>
  </svg>

  <!-- Sweet Soy Sauce -->
  <svg class="lid lid--soy" viewBox="0 0 236 267" aria-label="Sweet Soy Sauce lid">
    <defs><clipPath id="clip-soy"><rect width="236" height="267" rx="10"/></clipPath></defs>
    <g clip-path="url(#clip-soy)">
      <rect class="bg-black" width="236" height="267"/>
      <text class="display fill-orange" x="-1" y="54" font-size="72" textLength="238" lengthAdjust="spacingAndGlyphs">Sweet</text>
      <text class="display fill-white" x="0" y="164" font-size="140" textLength="236" lengthAdjust="spacingAndGlyphs">Soy</text>
      <text class="display fill-orange" x="-1" y="204" font-size="58" textLength="162" lengthAdjust="spacingAndGlyphs">Sauce</text>
      <text class="display fill-white" x="118" y="222" font-size="15" text-anchor="middle" textLength="226" lengthAdjust="spacingAndGlyphs">Thick, Rich Sweet &amp; Caramel-like</text>
      <text class="display fill-white" x="20" y="248" font-size="18">Wokly8</text>
      <text class="weight fill-white" x="223" y="248" font-size="16" text-anchor="end">NET WT 2 OZ</text>
    </g>
  </svg>

  <!-- Sweet Red Sauce -->
  <svg class="lid lid--sweet-red" viewBox="0 0 236 267" aria-label="Sweet Red Sauce lid">
    <defs><clipPath id="clip-sweet-red"><rect width="236" height="267" rx="10"/></clipPath></defs>
    <g clip-path="url(#clip-sweet-red)">
      <rect class="bg-orange" width="236" height="267"/>
      <text class="display fill-white" x="-1" y="52" font-size="72" textLength="238" lengthAdjust="spacingAndGlyphs">Sweet</text>
      <text class="display fill-white" x="-1" y="144" font-size="124" textLength="238" lengthAdjust="spacingAndGlyphs">Red</text>
      <text class="display fill-white" x="-1" y="196" font-size="90" textLength="238" lengthAdjust="spacingAndGlyphs">Sauce</text>
      <text class="display fill-white" x="118" y="219" font-size="16" text-anchor="middle" textLength="226" lengthAdjust="spacingAndGlyphs">Mild Heat &amp; Vibrant Sweetness</text>
      <text class="display fill-white" x="14" y="249" font-size="18">Wokly8</text>
      <text class="weight fill-white" x="223" y="249" font-size="16" text-anchor="end">NET WT 2 OZ</text>
    </g>
  </svg>

</main>
</body>
</html>
```